Brisk Fern Co. needs a new Label for our bottle!

We need a creative label for our 8oz bottle of Brisk Fern Odor Eliminator concentrate. (see attachment for Label specifications). The winner of this contest will probably be used to complete the other products bottle labels we will be launching in the next few months as all of our labels will be similar to this design.
Updates

Reason: We have extended the contest 5 days. Please submit final designs. Thank you

Target Market(s)

Customers who are trying to get rid of an odor in their house or business

Industry/Entity Type

Cleaning Product

Colors

Designer to choose colors to be used in the design.

Requirements
Must have
• - A lemon on the front of the label that stands out so when people are scrolling product listings on zelvora that they stop on our listing.
• - Vintage old-fashioned look to label
• (Update 10/22) - The label will on a 8oz round amber bottle (see bottle picture at https://www.vesselpacksupply.com/item/Q517)
• (Update 10/22) - The website address "www.briskfernco.com" should be on back of label.
• (Update 10/22) - "Feedback or Questions? Please email customer@briskfernco.com"
• (see attachment for Label specifications)
Nice to have
Should not have

```html
<!DOCTYPE html>
<html lang="en">
<head>
<meta charset="utf-8">
<title>Brisk Fern Co. Odor Eliminator Label</title>
<link href="https://fonts.googleapis.com/css2?family=Alfa+Slab+One&family=Rye&family=IM+Fell+English+SC&display=swap" rel="stylesheet">
<style>
  :root {
    --page: #ffffff;
    --label-yellow: #e8b923;
    --label-yellow-light: #f0c93e;
    --ink-brown: #4a2410;
    --ink-brown-soft: #6b3a1c;
  }
  html, body {
    margin: 0;
    padding: 0;
    width: 900px;
    height: 1200px;
    overflow: hidden;
    background: var(--page);
  }
  .canvas {
    position: relative;
    width: 900px;
    height: 1200px;
  }
  .label {
    position: absolute;
    left: 40px;
    top: 170px;
    width: 820px;
    height: 860px;
    background: radial-gradient(ellipse at 50% 40%, var(--label-yellow-light) 0%, var(--label-yellow) 70%);
    color: var(--ink-brown);
  }
  .label-frame {
    position: absolute;
    inset: 0;
  }
  .brand-name {
    position: absolute;
    top: 118px;
    left: 0;
    width: 100%;
    text-align: center;
    font-family: "Alfa Slab One", serif;
    font-size: 92px;
    line-height: 1;
    letter-spacing: 1px;
    margin: 0;
    font-weight: 400;
  }
  .brand-name .brand-suffix {
    font-size: 34px;
    vertical-align: 4px;
    margin-left: 4px;
  }
  .lemon-art {
    position: absolute;
    left: 230px;
    top: 240px;
    width: 390px;
    height: 290px;
    border-radius: 145px;
    background: radial-gradient(circle at 40% 50%, var(--ink-brown-soft) 0%, var(--ink-brown) 70%);
  }
  .product-name {
    position: absolute;
    top: 548px;
    left: 0;
    width: 100%;
    text-align: center;
    font-family: "Rye", serif;
    font-size: 52px;
    letter-spacing: 6px;
    line-height: 1;
    margin: 0;
    font-weight: 400;
  }
  .use-list {
    position: absolute;
    top: 612px;
    left: 90px;
    width: 640px;
    text-align: center;
    font-family: "IM Fell English SC", serif;
    font-size: 27px;
    line-height: 32px;
    font-weight: 700;
    margin: 0;
  }
  .volume {
    position: absolute;
    top: 706px;
    left: 0;
    width: 100%;
    text-align: center;
    font-family: "IM Fell English SC", serif;
    font-size: 30px;
    letter-spacing: 2px;
    margin: 0;
  }
</style>
</head>
<body>
<main class="canvas">
  <section class="label">
    <svg class="label-frame" width="820" height="860" viewBox="0 0 820 860" aria-hidden="true">
      <path d="M58 22 H762 A36 36 0 0 0 798 58 V802 A36 36 0 0 0 762 838 H58 A36 36 0 0 0 22 802 V58 A36 36 0 0 0 58 22 Z"
            fill="none" stroke="var(--ink-brown)" stroke-width="3"/>
      <path d="M66 38 H754 A28 28 0 0 0 782 66 V794 A28 28 0 0 0 754 822 H66 A28 28 0 0 0 38 794 V66 A28 28 0 0 0 66 38 Z"
            fill="none" stroke="var(--ink-brown)" stroke-width="2" stroke-dasharray="8 6"/>
      <line x1="60" y1="92" x2="760" y2="92" stroke="var(--ink-brown)" stroke-width="2" stroke-dasharray="8 6"/>
      <line x1="60" y1="682" x2="760" y2="682" stroke="var(--ink-brown)" stroke-width="2" stroke-dasharray="8 6"/>
      <line x1="60" y1="762" x2="760" y2="762" stroke="var(--ink-brown)" stroke-width="2" stroke-dasharray="8 6"/>
    </svg>

    <h1 class="brand-name">BRISK FERN<span class="brand-suffix">co.</span></h1>

    <div class="lemon-art" role="img" aria-label="Lemon slice illustration with two leaves"></div>

    <h2 class="product-name">ODOR ELIMINATOR</h2>

    <p class="use-list">Pet Odors, Pet Urine, Carpet, Wood Floors,<br>Litter Boxes, Basements, Trash Containers.</p>

    <p class="volume">8 FL OZ (237 ML)</p>
  </section>
</main>
</body>
</html>
```